Aufkleberdesign für 3d Messdienstleistungen
Zielgruppe
3d Messdienstleistungen in Industrie, Architektur und Schiffbau
Aufgabenstellung
technisches Design, ansprechend, rational
Wir benötigen Aufkleber mit sehr kurzen Informationen über unsere Dienstleistung, die wir auf den Messobjekten bei unseren Kunden hinterlassen,
- Logo (vorhanden),
- Kontaktdaten,
- Dienstleistungen (Liste von 4-5 Schlagwörtern), (Kalibrierung von Laserprojektion, Industrievermessung, Kranbahnvermessung, Bauwerksvermessung)
- netter Hintergrund
A4, A5, A6 für Druck, Querformat

```html
<!DOCTYPE html>
<html lang="de">
<head>
<meta charset="utf-8">
<title>Nordmess 3D – Aufkleber</title>
<link href="https://fonts.googleapis.com/css2?family=Rajdhani:wght@400;500&display=swap" rel="stylesheet">
<style>
  :root {
    --stage: #e9e6e1;
    --ink-black: #000000;
    --navy: #14254d;
    --navy-deep: #0a1430;
    --text-white: #ffffff;
    --accent-blue: #1fa3e6;
  }
  * { margin: 0; padding: 0; box-sizing: border-box; }
  html, body {
    width: 807px; height: 1200px; overflow: hidden;
    background: var(--stage);
  }
  .sticker {
    position: absolute; left: 0; top: 315px;
    width: 807px; height: 570px;
    background: var(--ink-black);
    overflow: hidden;
    font-family: "Rajdhani", sans-serif;
  }
  .sticker__backdrop {
    position: absolute; inset: 0;
    background:
      radial-gradient(ellipse 70% 90% at 85% 40%, rgba(40,70,130,0.55), transparent 70%),
      linear-gradient(100deg, var(--ink-black) 38%, var(--navy-deep) 62%, var(--navy) 100%);
  }
  .brand {
    position: absolute; left: 44px; top: 92px;
    display: flex; align-items: center; gap: 16px;
  }
  .brand__mark {
    width: 34px; height: 34px;
    background: var(--accent-blue);
  }
  .brand__name {
    color: var(--text-white);
    font-weight: 400; font-size: 40px;
    letter-spacing: 8px;
  }
  .services {
    position: absolute; left: 26px; top: 236px;
    list-style: none;
  }
  .services__item {
    color: var(--text-white);
    font-weight: 500; font-size: 34px;
    line-height: 49px;
    display: flex; align-items: center;
  }
  .services__item::before {
    content: ""; display: inline-block;
    width: 14px; height: 2px; margin-right: 2px;
    background: var(--accent-blue);
  }
  .contact {
    position: absolute; left: 42px;
    display: flex; align-items: center; gap: 14px;
    color: var(--accent-blue);
    font-weight: 500;
  }
  .contact--phone { top: 454px; font-size: 36px; }
  .contact--mail { top: 516px; font-size: 33px; }
  .contact svg { flex: none; }
</style>
</head>
<body>
  <section class="sticker">
    <div class="sticker__backdrop" role="img" aria-label="Dunkelblauer technischer Hintergrund mit Netzwerklinien und Punkten"></div>

    <div class="brand">
      <span class="brand__mark"></span>
      <span class="brand__name">NORDMESS 3D</span>
    </div>

    <ul class="services">
      <li class="services__item">Kalibrierung von Laserprojektion</li>
      <li class="services__item">Industrievermessung</li>
      <li class="services__item">Kranbahnvermessung</li>
      <li class="services__item">Bauwerksvermessung</li>
    </ul>

    <div class="contact contact--phone">
      <svg width="44" height="42" viewBox="0 0 44 42" fill="none" stroke="var(--accent-blue)" stroke-width="2.2" stroke-linejoin="round">
        <path d="M6 4 L13 2 L19 12 L14 16 C16 22 21 27 27 30 L31 25 L41 31 L39 38 C25 41 4 22 6 4 Z"/>
      </svg>
      <span>+ 49 (0)4321 - 5580172</span>
    </div>

    <div class="contact contact--mail">
      <svg width="44" height="34" viewBox="0 0 44 34" fill="none" stroke="var(--accent-blue)" stroke-width="2.4" stroke-linejoin="round">
        <rect x="2" y="2" width="40" height="30"/>
        <path d="M2 2 L22 19 L42 2"/>
      </svg>
      <span>info @ nordmess-3d.de</span>
    </div>
  </section>
</body>
</html>
```